Gestaltung eines Merkblattes
Ein Entwurf, der genau meinen Vorstellungen entspricht. Eine Abwicklung, die schneller und professioneller nicht sein könnte. Die Kommunikation - sehr symphatisch und kundenorientiert. Resumee: Besser geht es nicht.
Zielgruppe
www.tierklang-analytik.de/ Medizinische Bioresonanzanalysen für Pferde. Die Kundschaft besteht hauptsächlich aus Frauen, Alter von 20- 55 Jahre.
Bei dem Projekt handelt es sich um die Gestaltung eines wichtigen Merkblattes, das jedem Kunde zusammen mit dem Befund der Analyse gemailt wird. Es enthält wichtige Informationen rund um die Bioresonanzanalyse und sollte als pdf- Datei vorliegen.
Aufgabenstellung
Kernproblem: Die Kunden lesen das Merkblatt gar nicht oder nicht sorgfältig. So entstehen viele Fragen in der Folge, die nicht notwendig wären.
Wir benötigen eine pdf- Datei, die zum Lesen anregt, gerne gelesen wird und in der die wichtigsten Aspekte in das Auge fallen. Diese wurden von mir in der Worddatei, die den Text enthält, rot markiert.
Der Text in schwarz ist deutlich weniger wichtig.
Ach ja, die Überschrift ist doof. 'Allgemeine Hinweise' das animiert nicht wirklich zum Lesen. Falls Sie eine griffige Idee haben, sehr gerne.

```html
<!DOCTYPE html>
<html lang="de">
<head>
<meta charset="utf-8">
<title>Merkblatt – Wichtige Hinweise für die Bioresonanzanalysen</title>
<link href="https://fonts.googleapis.com/css2?family=Ubuntu:wght@300;400;500;700&display=swap" rel="stylesheet">
<style>
  :root{
    --green:#b7c073;
    --green-dark:#8e9158;
    --ink:#2a2a2a;
    --body-dark:#3a3a3a;
    --white:#ffffff;
    --paper-shadow:rgba(0,0,0,.28);
  }
  *{box-sizing:border-box;margin:0;padding:0}
  html,body{width:1200px;height:625px;overflow:hidden;background:var(--white)}
  body{position:relative;font-family:'Ubuntu',sans-serif;font-weight:300;color:var(--white)}
  .spread{position:absolute;top:34px;width:543px;height:544px;display:grid;grid-template-columns:271.5px 271.5px;grid-template-rows:272px 272px;box-shadow:2px 3px 5px var(--paper-shadow)}
  .spread--left{left:46px}
  .spread--right{left:609px}
  .panel{position:relative;overflow:hidden;padding-top:9px}
  .panel--outer{padding-left:19px;padding-right:9px}
  .panel--inner{padding-left:9.5px;padding-right:17px}
  .panel--green{background:var(--green);color:var(--white)}
  .panel--white{background:var(--white);color:var(--body-dark)}
  .panel__title{font-weight:500;font-size:12px;line-height:14px;white-space:nowrap}
  .panel--white .panel__title{color:var(--ink)}
  .panel__rule{display:block;width:47px;height:2px;margin:6px 0 10px;background:var(--green-dark)}
  .panel--white .panel__rule{background:var(--green)}
  .copy{position:relative;z-index:2;font-size:5.8px;line-height:9.7px;text-align:justify}
  .copy p{margin-bottom:9.7px}
  .copy b{font-weight:700}
  .photo{position:absolute;z-index:1}
  .nav{position:absolute;z-index:3;width:25px;height:25px;border-radius:50%;background:var(--white);display:flex;align-items:center;justify-content:center}
  .nav svg{width:15px;height:15px}
  .nav--soft{background:rgba(183,192,115,.85)}

  /* Titelseite */
  .cover{padding:0;background:var(--white)}
  .cover__photo{left:0;top:0;width:175px;height:272px;background:linear-gradient(90deg,#5e7a3a 0%,#7c9650 45%,#a9b98a 80%,rgba(255,255,255,0) 100%)}
  .cover__title{position:absolute;z-index:2;left:18px;top:212px;font-weight:700;font-size:11px;line-height:15px;color:var(--white);text-shadow:0 0 3px rgba(0,0,0,.35)}
  .brand{position:absolute;left:182px;top:58px;width:80px;display:flex;align-items:center;gap:4px;font-weight:500;font-size:8px;line-height:10px;color:var(--green-dark)}
  .brand__dot{width:7px;height:7px;border-radius:50%;background:var(--green);flex:none}
  .url-pill{position:absolute;left:184px;top:246px;width:88px;height:16px;background:var(--green);border-radius:8px 0 0 8px;font-size:5.8px;line-height:16px;padding-left:8px;color:var(--white)}

  /* Bachblüten-Anleitung */
  .recipe{display:flex;align-items:flex-end;justify-content:space-between;width:236px;margin:2px 0 3px 1px}
  .recipe__item{display:flex;flex-direction:column;align-items:center;font-weight:500;font-size:5.6px}
  .recipe__item svg{margin-bottom:5px}
  .recipe__plus{font-weight:700;font-size:16px;color:#8a8d62;margin-bottom:14px}
  .tiny{font-size:3.6px}
</style>
</head>
<body>

<section class="spread spread--left">

  <div class="panel cover">
    <div class="photo cover__photo" role="img" aria-label="Foto: junge Frau küsst einen Schimmel am Halfter vor grünem Laub"></div>
    <div class="brand"><span class="brand__dot"></span><span>Tierklang Analytik</span></div>
    <div class="nav" style="left:237px;top:148px;background:var(--green)">
      <svg viewBox="0 0 16 16"><path d="M3 8h9M8.5 4l4 4-4 4" fill="none" stroke="#fff" stroke-width="2.4" stroke-linecap="round" stroke-linejoin="round"/></svg>
    </div>
    <h1 class="cover__title">Wichtige Hinweise für die<br>Bioresonanzanalysen</h1>
    <div class="url-pill">www.tierklang-analytik.de</div>
  </div>

  <div class="panel panel--inner panel--green">
    <h2 class="panel__title">Das wichtigste zuerst</h2>
    <span class="panel__rule"></span>
    <div class="copy">
      <p>Die <b>empfohlenen Präparate</b> können (wenn nicht anders angegeben) <b>in das normale Kraftfutter</b> gegeben werden. <b>Tropfen</b> und <b>Bachblüten</b> bitte <b>auf</b> ein <b>kleines Stück trockenes Brot, Zwieback</b>, bei Pferden, die kein Getreide fressen dürfen, auf ein Stück Reiswaffel geben, und dem Pferd direkt füttern.</p>
      <p><b>Vitabase Pulver</b> muss <b>nicht</b>, wie vom Hersteller angegeben, <b>in Wasser aufgelöst werden</b>. Eine Gabe in das Kraftfutter, Heucobs etc. vermindert nicht die Wirkung.</p>
      <p style="width:196px;text-align:left">Bitte füttern Sie <b>alle Präparate</b>, außer es sind abweichende Empfehlungen vorhanden, <b>ohne Unterbrechung</b>, bis Ihnen das Ergebnis der ersten Nachtestung vorliegt. Pausen von mehr als zwei Tagen können zu Beginn der Behandlung die positive Entwicklung Ihres Pferdes beeinträchtigen.</p>
      <p style="width:163px;text-align:left">Falls Ihr <b>Pferd</b> sehr <b>wählerisch</b> ist bei der Zufütterung von Präparaten in Pellets- oder Pulverform, dann <b>beginnen</b> Sie mit einer <b>sehr kleinen Dosierung</b> von z. b. ½ <b>Teelöffel</b> und steigern diese sehr langsam. Bei trockenem Futter (Müsli, Hafer) sortieren manche Pferde gerne aus. Hier ist es sinnvoll, das <b>Futter anzufeuchten</b>, etwas Heucobs oder getreidefreies Mash dazuzugeben.</p>
    </div>
    <div class="photo" style="left:176px;top:178px;width:96px;height:94px;background:linear-gradient(160deg,#b7c073 0%,#7a4a2a 30%,#5a3a22 70%,#8a7a5a 100%);border-radius:40px 0 0 0" role="img" aria-label="Foto: Fuchspferd mit Blesse schaut über eine Stalltür an der Heuraufe"></div>
    <div class="nav" style="left:152px;top:238px">
      <svg viewBox="0 0 16 16"><path d="M8 3v9M4 8.5l4 4 4-4" fill="none" stroke="#8a8d62" stroke-width="2.4" stroke-linecap="round" stroke-linejoin="round"/></svg>
    </div>
  </div>

  <div class="panel panel--outer panel--green">
    <h2 class="panel__title">Bachblüten</h2>
    <span class="panel__rule"></span>
    <div class="copy">
      <p>Wenn die <b>Therapieempfehlung</b> eine <b>Übersicht an Bachblüten enthält</b>, dann <b>spiegeln diese den seelischen Zustand Ihres Pferdes wieder</b>, der von seinen aktuellen Lebensbedingungen, seiner körperlichen Belastung durch Krankheit und durch Abläufe in seiner Herde beeinflusst wird. Erfahrungsgemäß bezieht sich die <b>Darstellung</b> der Blüten bei Pferden, die in einer Herde leben, häufig mehr auf die <b>Gefühle des Pferdes gegenüber seinen Artgenossen</b> als auf den Kontakt mit dem Menschen.</p>
      <p>Die meisten <b>Apotheken kennen sich aus</b> mit der <b>Herstellung</b> einer <b>Bachblütenmischung</b>.</p>
      <p style="margin-bottom:4px"><b>Falls nicht, hier die Anleitung:</b></p>
    </div>
    <div class="recipe">
      <div class="recipe__item">
        <svg width="16" height="40" viewBox="0 0 16 42"><rect x="6" y="0" width="4" height="6" fill="#fff"/><path d="M5 7h6v4l4 5v26H1V16l4-5z" fill="#fff"/><rect x="3" y="20" width="10" height="15" fill="#b7c073"/></svg>
        <span>10 ml Alkohol</span>
      </div>
      <span class="recipe__plus">+</span>
      <div class="recipe__item">
        <svg width="16" height="40" viewBox="0 0 16 42"><rect x="6" y="0" width="4" height="6" fill="#fff"/><path d="M5 7h6v4l4 5v26H1V16l4-5z" fill="#fff"/></svg>
        <span>20 ml Quellwasser</span>
      </div>
      <span class="recipe__plus">+</span>
      <div class="recipe__item">
        <svg width="29" height="29" viewBox="0 0 30 30"><g fill="#fff"><circle cx="15" cy="5" r="5"/><circle cx="15" cy="25" r="5"/><circle cx="5" cy="15" r="5"/><circle cx="25" cy="15" r="5"/><circle cx="8" cy="8" r="5"/><circle cx="22" cy="8" r="5"/><circle cx="8" cy="22" r="5"/><circle cx="22" cy="22" r="5"/></g><circle cx="15" cy="15" r="4" fill="#b7c073"/></svg>
        <span>2-3 Tropfen jeder Blüte</span>
      </div>
    </div>
    <div class="copy">
      <p>in ein 30 ml Medizinfläschchen mit Tropfvorrichtung oder Pipette gibt man 10 ml Alkohol (Brandy oder Weinbrand), 20 ml Quellwasser oder stilles Mineralwasser (ohne Kohlensäure; kein destilliertes Wasser!) und 2-3 Tropfen von jeder Blüte, die im Moment benötigt wird. <span class="tiny">Als Alternative zu Alkohol kann auch Obstessig eingesetzt werden.</span></p>
    </div>
    <div class="nav" style="left:226px;top:237px">
      <svg viewBox="0 0 16 16"><path d="M8 3v9M4 8.5l4 4 4-4" fill="none" stroke="#8a8d62" stroke-width="2.4" stroke-linecap="round" stroke-linejoin="round"/></svg>
    </div>
  </div>

  <div class="panel panel--inner panel--white">
    <h2 class="panel__title">Nachtestung</h2>
    <span class="panel__rule"></span>
    <div class="copy">
      <p>Wir <b>bestätigen</b> den Eingang der Probe zur <b>Nachtestung nicht</b>. In regelmäßigen Abständen werden alle Befunde nachgetestet. Wir senden Ihnen im Anschluss per Mail das neue Ergebnis mit einer aktualisierten Therapieempfehlung zu.</p>
      <p>Wir brauchen für die <b>Nachtestung eine neue Haarprobe</b> und ein <b>kurzes Feedback</b> zu der <b>aktuellen Entwicklung</b> Ihres Pferdes. <b>Mehr nicht.</b></p>
    </div>
    <div class="photo" style="left:0;top:104px;width:271.5px;height:168px;background:linear-gradient(120deg,#c9a98a 0%,#6a3f2a 30%,#4e2e20 60%,#7a5a48 100%)" role="img" aria-label="Foto: Tierärztin hört ein braunes Pferd mit dem Stethoskop ab"></div>
    <div class="nav" style="left:14px;top:234px">
      <svg viewBox="0 0 16 16"><path d="M13 8H4M7.5 4l-4 4 4 4" fill="none" stroke="#3a3a3a" stroke-width="2.4" stroke-linecap="round" stroke-linejoin="round"/></svg>
    </div>
  </div>
</section>

<section class="spread spread--right">

  <div class="panel panel--outer panel--green">
    <h2 class="panel__title">Tierarzt</h2>
    <span class="panel__rule"></span>
    <div class="copy">
      <p><b>Wir weisen ausdrücklich darauf hin, dass die Ergebnisse der Bioresonanzanalyse nicht kompatibel sind mit den herkömmlichen Labormethoden und anderen tierärztlichen Diagnoseformen.</b></p>
      <p><b>Ein Beispiel:</b> Wenn wir eine Belastung der Leber mit dem Leberegel Fasciola hepatica feststellen, <b>kann</b> eine <b>klassische Laboruntersuchung</b> zu dem gleichen Thema <b>ergebnislos bleiben</b>. Der Grund hierfür liegt u. a. in der <b>sehr unterschiedlichen Beurteilung</b> und <b>Herangehensweise</b>.</p>
      <p style="width:176px;text-align:left">Das Wohl Ihres Pferdes steht jederzeit im Mittelpunkt. Falls <b>in der Zeit der Umsetzung der Therapie-empfehlung</b> bei Ihrem <b>Pferd Symptome auftreten</b>, die eine tierärztliche und schnelle Hilfe dringend erforderlich machen, <b>zögern Sie bitte nie, den Tierarzt zu rufen</b>.</p>
      <p style="width:176px;text-align:left">Bitte <b>informieren</b> Sie mich vorab, <b>wenn Ihr Pferd zum Zeitpunkt der Nachtestung Medikamente von dem Tierarzt erhält</b>. Relevant sind <b>Antibiotika, Cortison</b>, sowie andere, <b>massiv entzündungshemmende Präparate</b>. In diesem Fall sprechen wir miteinander ab, ob die Nachtestung verschoben wird. Wurmkuren und Impfungen sind für die Durchführung der Nachtestung nicht von Bedeutung.</p>
    </div>
    <div class="photo" style="left:200px;top:140px;width:72px;height:132px;background:linear-gradient(180deg,#b7c073 0%,#dfe2dc 30%,#eef0ee 70%,#c8ccc4 100%);border-radius:36px 0 0 0" role="img" aria-label="Foto: lächelnde Tierärztin im Kittel umarmt einen Schimmel"></div>
    <div class="nav" style="left:235px;top:237px">
      <svg viewBox="0 0 16 16"><path d="M3 8h9M8.5 4l4 4-4 4" fill="none" stroke="#8a8d62" stroke-width="2.4" stroke-linecap="round" stroke-linejoin="round"/></svg>
    </div>
  </div>

  <div class="panel panel--inner panel--white">
    <h2 class="panel__title">Impfung</h2>
    <span class="panel__rule"></span>
    <div class="copy">
      <p>Wir geben generell <b>keine Impfempfehlungen</b>. Es hat sich jedoch in den vergangenen Jahren gezeigt, dass es <b>sinnvoll</b> ist, <b>Impfungen</b> (besonders Influenza- und Herpes-Impfungen) vor Beginn der Umsetzung der <b>Therapieempfehlung einzuplanen</b>. Werden sie zu einem späteren Zeitpunkt vorgenommen, kann es zu Rückschritten in der ansonsten positiven Entwicklung kommen.</p>
    </div>
    <div class="photo" style="left:0;top:105px;width:271.5px;height:167px;background:linear-gradient(100deg,#c8d0b8 0%,#8e8e8a 30%,#b8b8b4 55%,#e8e8e6 80%,#9aa0a8 100%)" role="img" aria-label="Foto: Tierärztin mit Handschuhen impft einen Apfelschimmel am Hals"></div>
    <div class="nav nav--soft" style="left:122px;top:237px">
      <svg viewBox="0 0 16 16"><path d="M8 3v9M4 8.5l4 4 4-4" fill="none" stroke="#fff" stroke-width="2.4" stroke-linecap="round" stroke-linejoin="round"/></svg>
    </div>
  </div>

  <div class="panel panel--outer panel--white">
    <h2 class="panel__title">Tragende Stuten/ Stuten mit Fohlen bei Fuß</h2>
    <span class="panel__rule"></span>
    <div class="copy">
      <p><b>Wir übernehmen keine Haftung</b> für die Gabe der von uns empfohlenen Naturheilmittel <b>bei tragenden Stute und Stuten mit Fohlen</b> bei Fuß. Jedes der angegebenen Mittel wurde von mir mit großer Sorgfalt ausgewählt. Die aktuell vorhandenen, medizinischen Studien zu der Wirkung von Naturheilmitteln bei tragenden Stuten sind jedoch nicht umfangreich genug, um Nebenwirkungen vollständig ausschließen zu können.</p>
    </div>
    <div class="photo" style="left:0;top:97px;width:271.5px;height:175px;background:linear-gradient(175deg,#6a9ed0 0%,#a8c8e4 30%,#d8dcd8 55%,#8a5a3a 75%,#6a8a4a 100%)" role="img" aria-label="Foto: Schimmelstute und braunes Fohlen auf der Weide vor blauem Himmel"></div>
    <div class="nav" style="left:235px;top:228px">
      <svg viewBox="0 0 16 16"><path d="M3 8h9M8.5 4l4 4-4 4" fill="none" stroke="#3a3a3a" stroke-width="2.4" stroke-linecap="round" stroke-linejoin="round"/></svg>
    </div>
  </div>

  <div class="panel panel--inner panel--green">
    <h2 class="panel__title">Doping</h2>
    <span class="panel__rule"></span>
    <div class="copy">
      <p><b>Zum Schutz der Pferde bestehen Anti- Doping Richtlinien</b>, die klare Regeln vorgeben, welche Zu- satzfutterpräparate, Medikamente und auch Naturheilmittel einem Turnierpferd vor und während einem Start in einer Turnierprüfung gefüttert werden dürfen. Die Einhaltung der Vorgaben wird durch stichpunktartige Kontrollen überprüft.</p>
      <p>Bitte beachten Sie die Anti- Doping Richtlinien des Reitverbands und weiterer Pferdesportverbände und halten Sie bei der Fütterung aller Präparate unserer Therapieempfehlung eine Karenzzeit von 48 Stunden vor Prüfungsbeginn ein, wenn Sie mit Ihrem Pferd an einem Wettbewerb teilnehmen. <span style="display:inline">Ausnahme! Bei der Zufütterung von Präparaten, die Teufelskralle enthalten, besteht eine Karenzzeit von 4 Tagen.</span></p>
      <p style="width:117px;text-align:left"><b>Wir übernehmen für die Folgen einer Nichtbeachtung der nationalen oder internationalen Anti- Dopingrichtlinien keine Haftung.</b></p>
    </div>
    <div class="photo" style="left:150px;top:150px;width:122px;height:122px;background:radial-gradient(ellipse at 55% 65%,#b86a3a 0%,#9a552c 45%,rgba(183,192,115,0) 72%)" role="img" aria-label="Foto: Fuchspferd mit Halfter, freigestellt"></div>
  </div>
</section>

</body>
</html>
```